Belle Journée Weddings and Events

I am a small boutique wedding coordinator, stylist and bridal consultant/coach/assistant. I am based in Brisbane, Australia and my business is geared towards mid range- high end budget bridal couples.
I am after some business cards that are double sided, with the logo on one side and all other information on the other side, including the business tagline of design, create, celebrate. The look of the card needs to be clean and crisp, with white and the tones of grey of the logo.The final design needs to convey sophistication and poise. Perhaps the logo and tagline could be done in a metallic silver with the rest of the text in the shades of grey from the style guide attached below.
Title- Mirela Tostavanque - Director / Events Manager and Stylist
Address - 218 Hollis Terrace, Marwick Vale, QLD, 4067
Phone- 07 3482 9517
Mobile- 0418 572 906
Email- Mirela@bellejourneeevents.com.au
Website- www.bellejourneeevents.com.au

```html
<!DOCTYPE html>
<html lang="en">
<head>
<meta charset="UTF-8">
<title>Belle Journée Weddings and Events – Business Cards</title>
<link rel="stylesheet" href="https://fonts.googleapis.com/css2?family=Mulish:wght@400;700&display=swap">
<style>
  :root {
    --canvas-bg: #e9e9ea;
    --card-white: #ffffff;
    --card-grey: #8e8e90;
    --ink-dark: #3c3c3e;
    --ink-mid: #6f6f72;
    --ink-light: #a4a4a7;
    --silver: #ececee;
    --silver-soft: #d4d4d7;
  }
  * { box-sizing: border-box; margin: 0; padding: 0; }
  html, body {
    width: 1200px; height: 800px; overflow: hidden;
    background: var(--canvas-bg);
    font-family: "Mulish", "Century Gothic", sans-serif;
  }
  .canvas {
    width: 1200px; height: 800px;
    display: flex; align-items: center; justify-content: center; gap: 60px;
  }
  .card {
    position: relative;
    width: 510px; height: 312px;
    border-radius: 4px;
    box-shadow: 0 10px 28px rgba(0,0,0,0.14), 0 2px 6px rgba(0,0,0,0.08);
    overflow: hidden;
  }

  /* Information side */
  .card--info { background: var(--card-white); color: var(--ink-mid); }
  .contact-name {
    position: absolute; left: 30px; top: 26px;
    font-weight: 700; font-size: 22px; color: var(--ink-dark); letter-spacing: 0.2px;
  }
  .contact-title {
    position: absolute; left: 30px; top: 56px;
    font-size: 13px; color: var(--ink-light);
  }
  .contact-lines {
    position: absolute; left: 30px; top: 82px;
    list-style: none; font-size: 13px; color: var(--ink-mid);
  }
  .contact-lines li { display: flex; align-items: center; gap: 7px; height: 20px; }
  .contact-lines b { font-weight: 700; color: var(--ink-dark); }
  .icon { width: 12px; height: 12px; flex: none; }
  .phone-lines {
    position: absolute; left: 225px; top: 160px;
    list-style: none; font-size: 15px; color: var(--ink-mid);
  }
  .phone-lines li { display: flex; align-items: center; gap: 7px; height: 22px; }
  .address {
    position: absolute; left: 30px; top: 218px;
    font-weight: 700; font-size: 15px; color: var(--ink-dark); line-height: 20px;
    text-align: right; width: 230px;
  }
  .tagline {
    position: absolute; left: 24px; bottom: 20px;
    font-size: 21px; color: var(--ink-light); letter-spacing: 0.3px;
  }
  .brand-small {
    position: absolute; right: 30px; top: 140px; width: 150px;
    text-align: center; color: var(--ink-mid);
  }
  .brand-small .brand-name { font-size: 20px; }
  .brand-small .brand-sub { font-size: 10px; margin-top: 3px; }

  /* Logo side */
  .card--logo { background: var(--card-grey); color: var(--silver); }
  .brand-large {
    position: absolute; left: 190px; top: 66px; width: 280px;
    text-align: center;
  }
  .brand-large .brand-name { font-size: 40px; color: var(--silver); }
  .brand-large .brand-sub { font-size: 14px; color: var(--silver); margin-top: 6px; }
  .card--logo .tagline {
    color: #ffffff; font-size: 28px; left: 26px; bottom: 28px;
  }
</style>
</head>
<body>
<main class="canvas">

  <section class="card card--info" aria-label="Business card, information side">
    <h1 class="contact-name">Mirela Tostavanque</h1>
    <p class="contact-title">Director / Events Manager / Stylist</p>
    <ul class="contact-lines">
      <li>
        <svg class="icon" viewBox="0 0 12 12" aria-hidden="true"><rect x="0.5" y="2" width="11" height="8" rx="1" fill="var(--ink-dark)"/><path d="M1 2.8 L6 6.6 L11 2.8" stroke="#fff" stroke-width="1" fill="none"/></svg>
        <span>mirela@<b>bellejourneeevents</b>.com.au</span>
      </li>
      <li>
        <svg class="icon" viewBox="0 0 12 12" aria-hidden="true"><circle cx="6" cy="6" r="5.5" fill="var(--ink-dark)"/><path d="M0.8 6 H11.2 M6 0.6 C3 3 3 9 6 11.4 M6 0.6 C9 3 9 9 6 11.4" stroke="#fff" stroke-width="0.8" fill="none"/></svg>
        <span>www.<b>bellejourneeevents</b>.com.au</span>
      </li>
    </ul>

    <div class="brand-small">
      <div class="brand-name">Belle Journée</div>
      <div class="brand-sub">Weddings &amp; Events</div>
    </div>

    <ul class="phone-lines">
      <li>
        <svg class="icon" viewBox="0 0 12 12" aria-hidden="true"><path d="M2.5 0.8 L4.4 3.2 L3.4 4.6 C4.2 6.2 5.6 7.6 7.2 8.5 L8.6 7.5 L11 9.4 L9.8 11.2 C5.2 10.8 1.2 6.8 0.8 2.2 Z" fill="var(--ink-dark)"/></svg>
        <span>07 3482 9517</span>
      </li>
      <li>
        <svg class="icon" viewBox="0 0 12 12" aria-hidden="true"><rect x="3" y="0.5" width="6" height="11" rx="1" fill="var(--ink-dark)"/><rect x="4" y="2" width="4" height="6.5" fill="#fff"/></svg>
        <span>0418 572 906</span>
      </li>
    </ul>

    <address class="address">218 Hollis Terrace<br>Marwick Vale, QLD, 4067</address>

    <p class="tagline">•design •create •celebrate•</p>
  </section>

  <section class="card card--logo" aria-label="Business card, logo side">
    <div class="brand-large">
      <div class="brand-name">Belle Journée</div>
      <div class="brand-sub">Weddings &amp; Events</div>
    </div>
    <p class="tagline">•design •create •celebrate•</p>
  </section>

</main>
</body>
</html>
```